Non-profit needs fresh graphics for online fundraiser.

We are wanting some fresh, spring-themed graphics for our spring online auction fundraiser. We are a faith based non-profit that serves families who have a child facing a devastating medical crisis. The design we go with will be used for multiple things...banners, ZV posts, auction website etc...

Target Market(s)

These will be used for social media advertising, email marketing, and on our custom auction website.

Industry/Entity Type

Non-Profit

Font styles to use
Decorative
Script

Requirements
Must have
• This title: MARV's Foundation Spring Online Auction or MARV's Foundation Spring Bid-O-Rama
Nice to have
• Maybe include our logo but not as the centerpiece. Possibly some flowers or watercolor effects but hoping to see ideas beyond these parameters also.
Should not have
• Dark colors

```html
<!DOCTYPE html>
<html lang="en">
<head>
<meta charset="utf-8">
<title>MARV's Foundation Spring Online Auction</title>
<link rel="stylesheet" href="https://fonts.googleapis.com/css2?family=Quicksand:wght@500&family=Norican&display=swap">
<style>
  :root {
    --cream: #f8f6ee;
    --leaf-green: #b9cbb0;
    --leaf-lavender: #c4c0e2;
    --leaf-blue: #b8c6e4;
    --petal-pink: #e6a7d6;
    --petal-yellow: #f5e489;
    --paper-white: #ffffff;
    --title-teal: #12b3e0;
    --spring-pink: #d07cc0;
    --auction-orange: #f28c33;
  }
  html, body {
    margin: 0;
    padding: 0;
    width: 1200px;
    height: 1200px;
    overflow: hidden;
    background: var(--cream);
  }
  .poster {
    position: relative;
    width: 1200px;
    height: 1200px;
    overflow: hidden;
    background: var(--cream);
  }
  .botanical-backdrop {
    position: absolute;
    inset: 0;
    background:
      radial-gradient(circle at 12% 15%, rgba(185,203,176,0.85) 0, rgba(185,203,176,0) 32%),
      radial-gradient(circle at 35% 12%, rgba(196,192,226,0.75) 0, rgba(196,192,226,0) 26%),
      radial-gradient(circle at 72% 14%, rgba(184,198,228,0.75) 0, rgba(184,198,228,0) 28%),
      radial-gradient(circle at 74% 13%, rgba(230,167,214,0.6) 0, rgba(230,167,214,0) 10%),
      radial-gradient(circle at 50% 5%, rgba(245,228,137,0.6) 0, rgba(245,228,137,0) 12%),
      radial-gradient(circle at 92% 40%, rgba(185,203,176,0.8) 0, rgba(185,203,176,0) 30%),
      radial-gradient(circle at 8% 60%, rgba(184,198,228,0.85) 0, rgba(184,198,228,0) 32%),
      radial-gradient(circle at 90% 75%, rgba(196,192,226,0.7) 0, rgba(196,192,226,0) 30%),
      radial-gradient(circle at 30% 92%, rgba(185,203,176,0.85) 0, rgba(185,203,176,0) 30%),
      radial-gradient(circle at 56% 86%, rgba(245,228,137,0.55) 0, rgba(245,228,137,0) 12%),
      radial-gradient(circle at 80% 95%, rgba(185,203,176,0.8) 0, rgba(185,203,176,0) 28%),
      var(--cream);
  }
  .brush-panel {
    position: absolute;
    left: 190px;
    top: 262px;
    width: 830px;
    height: 690px;
  }
  .title {
    position: absolute;
    left: 0;
    right: 0;
    top: 0;
    margin: 0;
    font-weight: normal;
    text-align: center;
  }
  .title span { position: absolute; left: 0; right: 0; display: block; white-space: nowrap; }
  .title-name {
    top: 318px;
    padding-left: 20px;
    font-family: "Quicksand", sans-serif;
    font-weight: 500;
    font-size: 132px;
    line-height: 1;
    color: var(--title-teal);
    letter-spacing: 1px;
  }
  .title-name small { font-size: 0.62em; vertical-align: 0.5em; margin-left: 2px; }
  .title-org {
    top: 420px;
    font-family: "Quicksand", sans-serif;
    font-weight: 500;
    font-size: 110px;
    line-height: 1;
    color: var(--title-teal);
    letter-spacing: 1px;
  }
  .title-season {
    top: 540px;
    font-family: "Norican", cursive;
    font-size: 190px;
    line-height: 1;
    color: var(--spring-pink);
  }
  .title-event {
    top: 760px;
    padding-left: 20px;
    font-family: "Norican", cursive;
    font-size: 100px;
    line-height: 1;
    color: var(--auction-orange);
  }
</style>
</head>
<body>
  <main class="poster">
    <div class="botanical-backdrop" role="img" aria-label="Soft watercolour pattern of green, lavender and blue leaves with small pink and yellow spring flowers"></div>

    <svg class="brush-panel" viewBox="0 0 830 690" aria-hidden="true">
      <path fill="var(--paper-white)" d="M70 40 C150 22 260 30 330 26 C420 18 520 30 610 24 C700 20 760 40 790 52 C810 110 800 170 812 230 C826 300 806 360 818 430 C828 500 812 560 820 620 C780 660 700 650 620 662 C520 676 420 660 320 670 C220 680 130 668 80 652 C60 600 70 560 64 500 C56 440 24 410 40 360 C54 310 30 270 20 230 C12 180 40 140 36 100 C34 70 50 52 70 40 Z"/>
    </svg>

    <h1 class="title">
      <span class="title-name">MARV'<small>s</small></span>
      <span class="title-org">Foundation</span>
      <span class="title-season">Spring</span>
      <span class="title-event">Online Auction</span>
    </h1>
  </main>
</body>
</html>
```